CRPG is needing business cards, and stationary created.

Pixel Forge created a logo for our business, and now we are wanting business cards, and stationary. I have included two designs of the same logo. Please feel free to use them as you want. The name of the company is Cedar Ridge Property Group LLC, the address is 812 NE Willow Ln., Suite 9, the city & state is Alder, Montana, zip code is 97815, Telephone number is 555-327-4489, Fax number is 555-327-6051, the name on the business card is Carl Whitby CMCA

Industry/Entity Type

Property Management

Contact Information for Business Card

The card needs to look professional. Upscale.

Requirements
Must have
• The colors we are using are on the logo that has been uploaded.

```html
<!DOCTYPE html>
<html lang="en">
<head>
<meta charset="utf-8">
<title>Cedar Ridge Property Group – Business Card</title>
<link rel="stylesheet" href="https://fonts.googleapis.com/css2?family=Open+Sans:wght@300;400;600&display=swap">
<style>
  :root {
    --backdrop: #d6d7da;
    --navy-light: #4d5668;
    --navy-dark: #272d3b;
    --teal: #3f8a72;
    --ink: #3a3f4a;
    --paper: #fbfbfa;
    --rule: #8fc3b0;
  }
  * { box-sizing: border-box; margin: 0; padding: 0; }
  html, body {
    width: 1200px; height: 800px; overflow: hidden;
    background: var(--backdrop);
    font-family: "Open Sans", sans-serif;
  }
  .sheet {
    position: relative; width: 1200px; height: 800px;
    display: flex; align-items: center; justify-content: center; gap: 60px;
  }
  .card {
    position: relative; width: 520px; height: 297px;
    border-radius: 4px; overflow: hidden;
    box-shadow: 0 6px 20px rgba(0,0,0,.18);
  }
  /* front */
  .card-front {
    background: linear-gradient(160deg, var(--navy-light) 0%, var(--navy-dark) 100%);
  }
  .front-brand {
    position: absolute; left: 290px; top: 78px;
    display: flex; align-items: center; gap: 12px;
  }
  .brand-square { width: 22px; height: 22px; background: var(--teal); }
  .front-brand .brand-name {
    font-size: 40px; font-weight: 600; color: #ffffff; letter-spacing: 2px;
  }
  .front-company {
    position: absolute; left: 170px; bottom: 26px;
    font-size: 13px; font-weight: 400; color: var(--teal); letter-spacing: .3px;
    white-space: nowrap;
  }
  /* back */
  .card-back { background: var(--paper); }
  .back-brand {
    position: absolute; left: 26px; top: 114px;
    display: flex; align-items: center; gap: 9px;
  }
  .back-brand .brand-square { width: 15px; height: 15px; flex: none; }
  .back-brand .brand-name {
    font-size: 19px; font-weight: 600; color: var(--teal); white-space: nowrap;
  }
  .divider {
    position: absolute; left: 212px; top: 70px; width: 1px; height: 170px;
    background: linear-gradient(to bottom, transparent, var(--rule) 20%, var(--rule) 80%, transparent);
  }
  .contact {
    position: absolute; left: 230px; top: 56px; right: 12px;
    color: var(--ink);
  }
  .contact-name { font-size: 20px; font-weight: 300; margin-bottom: 26px; white-space: nowrap; }
  .contact-name .credential { color: var(--teal); }
  .contact-address, .contact-lines {
    font-size: 10.5px; font-weight: 400; line-height: 1.55; white-space: nowrap;
  }
  .contact-address { margin-bottom: 18px; }
</style>
</head>
<body>
  <main class="sheet">
    <section class="card card-front" aria-label="Card front">
      <div class="front-brand">
        <span class="brand-square"></span>
        <span class="brand-name">CRPG</span>
      </div>
      <p class="front-company">Cedar Ridge Property Group LLC</p>
    </section>

    <section class="card card-back" aria-label="Card back">
      <div class="back-brand">
        <span class="brand-square"></span>
        <span class="brand-name">CEDAR RIDGE</span>
      </div>
      <div class="divider"></div>
      <div class="contact">
        <h1 class="contact-name">Carl Whitby <span class="credential">CMCA</span></h1>
        <p class="contact-address">
          Cedar Ridge Property Group LLC,<br>
          812 NE Willow Ln., Suite 9, the city &amp; state is Alder,<br>
          Montana, zip code 97815
        </p>
        <p class="contact-lines">
          Telephone: 555-327-4489<br>
          Fax: 555-327-6051
        </p>
      </div>
    </section>
  </main>
</body>
</html>
```